Four in One (Flexible infographic for Content Management Industry)

See attachment.
A graphic depicting 4 products, where each can stand on its own and each can be combined with others, but where, if all are taken together, the best result is achieved (the "super product").
Intended use is web. See attached file as an example.
The most basic idea is as the attached diagram shows, where 4 rectangles are arranged in a quadrangle, with a middle rectangle in the center representing the combined 4 products. This concept is fine except it is a bit too obvious as it stands. We are looking for either a variation of this or another concept.
The audience is technical + professional + enterprise - NOT consumers. Hence the design should be conservative in nature.
We are aware of tools like as Canva or Pictogram where such graphics are available, but we are looking for something with a bit more imagination and flexibility.
This graphic should be targeted to web sites and be delivered with vector-based (SVG) graphics.

```html
<!DOCTYPE html>
<html lang="en">
<head>
<meta charset="utf-8">
<title>Super Product</title>
<link rel="stylesheet" href="https://fonts.googleapis.com/css2?family=Lato:wght@400;700&display=swap">
<style>
  :root {
    --bg: #202227;
    --frame: #3b3e48;
    --card: #3e3f4c;
    --accent: #ef7300;
    --accent-text: #f07a18;
    --text: #d4d6df;
    --icon-light: #a8aab9;
    --icon-dark: #636a8f;
    --white: #ffffff;
  }
  * { box-sizing: border-box; margin: 0; padding: 0; }
  html, body { width: 1200px; height: 675px; overflow: hidden; background: var(--bg); }
  body { font-family: "Lato", sans-serif; color: var(--text); position: relative; }

  .frame {
    position: absolute; left: 51px; top: 57px; width: 1098px; height: 581px;
    border: 2px solid var(--frame); border-radius: 9px;
  }
  .badge {
    position: absolute; left: 460px; top: 23px; width: 280px; height: 60px;
    background: var(--accent); border: 2px solid #2a2c33; border-radius: 4px;
    display: flex; align-items: center; justify-content: center;
    color: var(--white); font-weight: 700; font-size: 31px; letter-spacing: 0.2px;
    box-shadow: 0 0 0 3px var(--bg);
  }
  .card {
    position: absolute; width: 530px; height: 255px;
    background: var(--card); border-radius: 8px;
  }
  .card--tl { left: 64px; top: 103px; }
  .card--tr { left: 606px; top: 103px; }
  .card--bl { left: 64px; top: 369px; }
  .card--br { left: 606px; top: 369px; }

  .card-icon { position: absolute; left: 0; top: 0; width: 170px; height: 254px; }

  .card-body { position: absolute; left: 170px; top: 24px; width: 340px; }
  .card-title { color: var(--accent-text); font-weight: 700; font-size: 20.5px; line-height: 24px; }
  .card-desc { margin-top: 9px; font-size: 15.3px; line-height: 18.75px; }
  .card-list { margin-top: 9px; list-style: none; font-size: 15.3px; line-height: 18.75px; }
  .card-list li { position: relative; padding-left: 16px; }
  .card-list li::before {
    content: ""; position: absolute; left: 2px; top: 8px; width: 5px; height: 5px;
    border-radius: 50%; background: var(--text);
  }
  .learn-more {
    display: inline-flex; align-items: center; gap: 9px; margin-top: 13px;
    color: var(--accent-text); font-weight: 700; font-size: 15.5px; text-decoration: none;
  }
  .learn-more svg { width: 22px; height: 20px; }
</style>
</head>
<body>
  <div class="frame"></div>
  <div class="badge">Super Product</div>

  <section class="card card--tl">
    <svg class="card-icon" viewBox="0 0 272 406" aria-hidden="true">
      <path d="M51 49 H165 L231 115 V267 q0 10 -10 10 H51 q-10 0 -10 -10 V59 q0 -10 10 -10Z" fill="var(--icon-light)"/>
      <path d="M165 49 L231 115 H173 q-8 0 -8 -8Z" fill="var(--icon-dark)"/>
      <polyline points="95,190 131,213 176,154" fill="none" stroke="var(--icon-dark)" stroke-width="17" stroke-linecap="round" stroke-linejoin="round"/>
    </svg>
    <div class="card-body">
      <h2 class="card-title">Document Management</h2>
      <p class="card-desc">Streamline document organization, access, and collaboration with easier file storage and sharing, leading to more efficient workflows.</p>
      <ul class="card-list">
        <li>Centralized Document Control</li>
        <li>Collaborative Workspace Integration</li>
        <li>Automated Compliance Tracking</li>
        <li>Check 4</li>
      </ul>
      <a class="learn-more" href="#">Learn More
        <svg viewBox="0 0 22 20"><path d="M2 10 H19 M11 2 L19 10 L11 18" fill="none" stroke="currentColor" stroke-width="2.6" stroke-linecap="round" stroke-linejoin="round"/></svg>
      </a>
    </div>
  </section>

  <section class="card card--tr">
    <svg class="card-icon" viewBox="0 0 272 406" aria-hidden="true">
      <g fill="var(--icon-light)">
        <circle cx="114" cy="100" r="57"/>
        <circle cx="184" cy="128" r="57"/>
        <circle cx="74" cy="140" r="45"/>
        <rect x="30" y="120" width="211" height="65" rx="40"/>
      </g>
      <path d="M135 114 q6 0 10 8 q20 12 38 12 q5 0 5 6 v38 q0 30 -53 52 q-53 -22 -53 -52 v-38 q0 -6 5 -6 q18 0 38 -12 q4 -8 10 -8Z" fill="var(--icon-dark)"/>
    </svg>
    <div class="card-body">
      <h2 class="card-title">Security and Compliance</h2>
      <p class="card-desc">Benefit from tailored cloud solutions, secure data storage, and expert disaster recovery planning for reliable and scalable IT operations.</p>
      <ul class="card-list">
        <li>Custom Cloud Solutions</li>
        <li>Secure Data Storage</li>
        <li>Expert Disaster Recovery</li>
        <li>Check 4</li>
      </ul>
      <a class="learn-more" href="#">Learn More
        <svg viewBox="0 0 22 20"><path d="M2 10 H19 M11 2 L19 10 L11 18" fill="none" stroke="currentColor" stroke-width="2.6" stroke-linecap="round" stroke-linejoin="round"/></svg>
      </a>
    </div>
  </section>

  <section class="card card--bl">
    <svg class="card-icon" viewBox="0 0 272 406" aria-hidden="true">
      <rect x="41" y="38" width="190" height="146" rx="18" fill="var(--icon-light)"/>
      <circle cx="106" cy="110" r="37" fill="var(--icon-dark)"/>
      <circle cx="187" cy="97" r="14" fill="var(--icon-dark)"/>
      <line x1="187" y1="100" x2="187" y2="134" stroke="var(--icon-dark)" stroke-width="13" stroke-linecap="round"/>
      <rect x="63" y="199" width="44" height="14" rx="7" fill="var(--icon-dark)"/>
      <rect x="165" y="199" width="44" height="14" rx="7" fill="var(--icon-dark)"/>
    </svg>
    <div class="card-body">
      <h2 class="card-title">Enterprice Resource Planning</h2>
      <p class="card-desc">Simplify management accross finance, sales, and operations, enabling better decisions-making and improved productivity.</p>
      <ul class="card-list">
        <li>Integrated Business Processes</li>
        <li>Enhanced Decisions-Making</li>
        <li>Productivity Improvement</li>
        <li>Check 4</li>
      </ul>
      <a class="learn-more" href="#">Learn More
        <svg viewBox="0 0 22 20"><path d="M2 10 H19 M11 2 L19 10 L11 18" fill="none" stroke="currentColor" stroke-width="2.6" stroke-linecap="round" stroke-linejoin="round"/></svg>
      </a>
    </div>
  </section>

  <section class="card card--br">
    <svg class="card-icon" viewBox="0 0 272 406" aria-hidden="true">
      <path d="M99 196 H171 L177 232 H93Z" fill="var(--icon-light)"/>
      <rect x="29" y="36" width="211" height="161" rx="18" fill="var(--icon-light)"/>
      <rect x="78" y="231" width="113" height="16" rx="8" fill="var(--icon-dark)"/>
      <path d="M134.5 68 q5 0 8 7 q18 10 34 10 q5 0 5 5 v34 q0 26 -47 44 q-47 -18 -47 -44 v-34 q0 -5 5 -5 q16 0 34 -10 q3 -7 8 -7Z" fill="var(--icon-dark)"/>
    </svg>
    <div class="card-body">
      <h2 class="card-title">Digital Transformation</h2>
      <p class="card-desc">Turn scanned documents into easily searchable digital archives, boosting efficiency and accessibility.</p>
      <ul class="card-list">
        <li>Instant searchable Archives with OCR</li>
        <li>Automated Document Classification</li>
        <li>Sharelume and Cloud Blob Ready</li>
        <li>Check 4</li>
      </ul>
      <a class="learn-more" href="#">Learn More
        <svg viewBox="0 0 22 20"><path d="M2 10 H19 M11 2 L19 10 L11 18" fill="none" stroke="currentColor" stroke-width="2.6" stroke-linecap="round" stroke-linejoin="round"/></svg>
      </a>
    </div>
  </section>
</body>
</html>
```